Orchid Wedding Stationary Design

We are looking for a number for designs for some wedding invitations:

1. A circular design like to Example_Sample - the colours are picked from the orchid picture (inner circle 8.5cm to be printed on A5 paper (the original files for this idea are included: Original and Original_Modified). Please feel free to have some fun with the colours!

2. The second design is like first except with the flowers/leaves framing a A5 page i.e. a square border rather than a circular one

3. The third is a design of a orchid (to be printed on an A6 page) in similar colours to Example_Sample in the style of the Flamelily image

Target Market(s)

N/A

Industry/Entity Type

Wedding

Colors
e34197
6c459b

Requirements
Must have
• 3 designs described above
Nice to have
• Nil
Should not have
• No font in the designs

```html
<!DOCTYPE html>
<html lang="en">
<head>
<meta charset="utf-8">
<title>Orchid Wedding Stationery – Card Set</title>
<link rel="stylesheet" href="https://fonts.googleapis.com/css2?family=Arimo:wght@400&display=swap">
<style>
  :root {
    --backdrop: #eceef0;
    --paper: #ffffff;
    --label: #a9a9a9;
    --guide: #b4b4b4;
    --measure: #555555;
    --pink: #f38fc0;
    --coral: #f7735e;
    --red: #f2424e;
    --peach: #f9b98a;
    --yellow: #f4e46a;
    --green: #6fe07a;
    --mint: #7fefd2;
    --blue: #4f78ee;
    --violet: #a48cf0;
    --lilac: #e6b6f2;
  }
  * { box-sizing: border-box; margin: 0; padding: 0; }
  html, body { width: 1200px; height: 923px; overflow: hidden; }
  body {
    background: radial-gradient(ellipse at 50% 50%, #fbfbfc 0%, #eceef0 55%, #c9cdd1 100%);
    font-family: "Arimo", Arial, sans-serif;
    position: relative;
  }
  .card {
    position: absolute;
    background: var(--paper);
    box-shadow: 0 1px 4px rgba(0,0,0,0.14);
  }
  .card--wreath { left: 31px; top: 169px; width: 410px; height: 582px; }
  .card--frame  { left: 455px; top: 171px; width: 411px; height: 582px; }
  .card--orchid { left: 881px; top: 257px; width: 291px; height: 409px; }

  .size-label {
    position: absolute;
    left: 0; right: 0;
    text-align: center;
    color: var(--label);
    font-size: 22px;
    line-height: 1;
    z-index: 2;
  }
  .card--wreath .size-label { top: 506px; }
  .card--frame .size-label  { top: 280px; }
  .card--orchid .size-label { top: 57px; }

  .wreath {
    position: absolute;
    left: 7px; top: 95px;
    width: 382px; height: 382px;
    border-radius: 50%;
    background: conic-gradient(from 0deg,
      var(--lilac), var(--violet), var(--blue), var(--peach), var(--coral),
      var(--peach), var(--pink), var(--mint), var(--green), var(--peach),
      var(--coral), var(--blue), var(--violet), var(--pink), var(--violet),
      var(--green), var(--pink), var(--lilac));
    -webkit-mask: radial-gradient(circle, transparent 0 112px, #000 124px 176px, transparent 191px);
            mask: radial-gradient(circle, transparent 0 112px, #000 124px 176px, transparent 191px);
    opacity: 0.7;
  }
  .measure {
    position: absolute;
    left: 80px; top: 168px;
    width: 236px; height: 236px;
  }
  .measure-text {
    font-family: "Arimo", Arial, sans-serif;
    font-size: 11px;
    fill: var(--measure);
  }

  .floral-border {
    position: absolute;
    inset: 2px;
    border: 58px solid transparent;
    border-image: linear-gradient(160deg,
      var(--coral), var(--pink), var(--coral), var(--violet), var(--blue),
      var(--green), var(--peach), var(--coral), var(--lilac), var(--mint)) 1;
    opacity: 0.6;
  }

  .orchid {
    position: absolute;
    left: 5px; top: 103px;
    width: 280px; height: 235px;
    border-radius: 46% 48% 40% 44%;
    background:
      radial-gradient(circle at 78% 25%, rgba(127,232,160,0.95) 0 22%, transparent 45%),
      radial-gradient(circle at 50% 12%, rgba(244,228,106,0.9) 0 14%, transparent 32%),
      radial-gradient(circle at 30% 85%, rgba(79,120,238,0.95) 0 12%, transparent 30%),
      radial-gradient(circle at 80% 70%, rgba(242,66,78,0.85) 0 14%, transparent 36%),
      radial-gradient(circle at 15% 55%, rgba(247,115,94,0.9) 0 20%, transparent 42%),
      linear-gradient(135deg, #f7a08a, #f38fc0 55%, #f2424e);
    opacity: 0.9;
  }
</style>
</head>
<body>

  <section class="card card--wreath">
    <div class="wreath" role="img" aria-label="Watercolour wreath of rainbow-toned leaves and small flowers"></div>
    <svg class="measure" viewBox="0 0 236 236">
      <defs>
        <marker id="arrow-head" viewBox="0 0 10 10" refX="10" refY="5" markerWidth="7" markerHeight="7" orient="auto-start-reverse">
          <path d="M0 0 L10 5 L0 10 z" fill="#777"/>
        </marker>
      </defs>
      <circle cx="118" cy="118" r="117" fill="none" stroke="var(--guide)" stroke-width="1"/>
      <line x1="3" y1="118" x2="94" y2="118" stroke="#777" stroke-width="1" marker-start="url(#arrow-head)"/>
      <line x1="142" y1="118" x2="233" y2="118" stroke="#777" stroke-width="1" marker-end="url(#arrow-head)"/>
      <text class="measure-text" x="118" y="122" text-anchor="middle">8.50 cm</text>
    </svg>
    <p class="size-label">A5</p>
  </section>

  <section class="card card--frame">
    <div class="floral-border" role="img" aria-label="Rectangular border of watercolour leaves and flowers in rainbow tones, orchid blooms in two corners"></div>
    <p class="size-label">A5</p>
  </section>

  <section class="card card--orchid">
    <p class="size-label">A6</p>
    <div class="orchid" role="img" aria-label="Watercolour orchid bloom in rainbow tones of coral, yellow, green, red and blue"></div>
  </section>

</body>
</html>
```